Milo Brennick Design, LLC: Die-Cut/Industrial Architecture Work

I have uploaded an amazing business card design which will be printed on stainless steel (metal). The logo does not need to change nor the card layout except as may be necessary to complete the project I am about to describe. THIS IS A DIE-CUT and STEEL BEAM IMAGERY PROJECT.

I am an architect and much of my work is steel structures. This business card project is focused exclusively taking the card design ("as is") to the next level of incredible by incorporating some type of die-cutting or creative imagery (maybe even abstract) of a steel beam which signifies the type of industrial architecture I do. Ultimately, when someone looks at this business card ... I want the card to have an "industrial" feel and it obvious that I do steel structures.

```html
<!DOCTYPE html>
<html lang="en">
<head>
<meta charset="utf-8">
<title>Milo Brennick Design, LLC — Business Card</title>
<link href="https://fonts.googleapis.com/css2?family=Montserrat:wght@600&family=Poppins:wght@400&family=Ubuntu:wght@400&display=swap" rel="stylesheet">
<style>
  :root {
    --backdrop: #2a2a2b;
    --steel-light: #f2f2f3;
    --steel-mid: #d9dadc;
    --steel-dark: #c4c5c8;
    --ink: #141414;
  }
  * { margin: 0; padding: 0; box-sizing: border-box; }
  html, body { width: 1104px; height: 1200px; overflow: hidden; }
  body {
    background: var(--backdrop);
    position: relative;
    font-family: "Poppins", sans-serif;
    color: var(--ink);
  }
  .card {
    position: absolute;
    left: 188px;
    width: 730px;
    height: 419px;
    border-radius: 16px;
    overflow: hidden;
    background:
      repeating-linear-gradient(0deg, rgba(255,255,255,0.18) 0 1px, rgba(0,0,0,0.03) 1px 2px),
      linear-gradient(160deg, var(--steel-mid) 0%, var(--steel-light) 45%, var(--steel-dark) 100%);
  }
  .card--front { top: 144px; }
  .card--back { top: 631px; }

  .wordmark__name {
    font-family: "Poppins", sans-serif;
    font-weight: 400;
    font-size: 44px;
    line-height: 1;
    letter-spacing: 0.5px;
    white-space: nowrap;
  }
  .wordmark__sub {
    font-family: "Montserrat", sans-serif;
    font-weight: 600;
    font-size: 17px;
    letter-spacing: 5px;
  }
  .wordmark__sub small { font-size: 12px; letter-spacing: 1px; margin-left: 4px; }

  .card--front .wordmark { position: absolute; left: 46px; top: 62px; text-align: center; width: 360px; }
  .card--front .wordmark__sub { margin-top: 24px; }

  .contacts { position: absolute; left: 44px; top: 230px; list-style: none; }
  .contacts li {
    display: flex; align-items: flex-start; gap: 10px;
    font-size: 16px; line-height: 24px; margin-bottom: 6px;
  }
  .contacts li.contacts__address { margin-top: 10px; }
  .contacts svg { width: 18px; height: 18px; flex: none; margin-top: 3px; }

  .beam-illustration {
    position: absolute; left: 432px; top: 0; width: 274px; height: 402px;
    background: linear-gradient(200deg, rgba(90,91,94,0.15) 0%, rgba(20,20,20,0.55) 100%);
    border-radius: 0 0 10px 10px;
  }

  .card--back .lockup {
    position: absolute; left: 139px; top: 134px;
    display: flex; align-items: center; gap: 18px;
  }
  .lockup__square { width: 82px; height: 82px; border: 3px solid var(--ink); }
  .lockup__divider { width: 2px; height: 154px; background: var(--ink); }
  .card--back .wordmark { text-align: center; width: 330px; }
  .card--back .wordmark__sub { margin-top: 18px; }

  .tagline {
    position: absolute; left: 0; right: 0; top: 354px;
    text-align: center;
    font-family: "Ubuntu", sans-serif;
    font-size: 19px;
  }
</style>
</head>
<body>
  <section class="card card--front">
    <div class="wordmark">
      <div class="wordmark__name">Milo Brennick</div>
      <div class="wordmark__sub">DESIGN<small>LLC</small></div>
    </div>

    <ul class="contacts">
      <li>
        <svg viewBox="0 0 24 24" fill="var(--ink)"><path d="M6.6 10.8a15.1 15.1 0 0 0 6.6 6.6l2.2-2.2c.3-.3.7-.4 1-.2 1.1.4 2.3.6 3.6.6.6 0 1 .4 1 1V20c0 .6-.4 1-1 1A17 17 0 0 1 3 4c0-.6.4-1 1-1h3.5c.6 0 1 .4 1 1 0 1.3.2 2.5.6 3.6.1.3 0 .7-.2 1z"/></svg>
        <span>415.260.3384</span>
      </li>
      <li>
        <svg viewBox="0 0 24 24" fill="var(--ink)"><path d="M3 5h18v14H3z"/><path d="M3 5l9 7 9-7" fill="none" stroke="#e6e6e8" stroke-width="1.6"/></svg>
        <span>milo@milobrennick.design</span>
      </li>
      <li>
        <svg viewBox="0 0 24 24" fill="none" stroke="var(--ink)" stroke-width="1.8"><circle cx="12" cy="12" r="9"/><ellipse cx="12" cy="12" rx="4" ry="9"/><path d="M3 12h18M4.5 7.5h15M4.5 16.5h15"/></svg>
        <span>www.milobrennick.design</span>
      </li>
      <li class="contacts__address">
        <svg viewBox="0 0 24 24" fill="var(--ink)"><path d="M12 2a7 7 0 0 0-7 7c0 5 7 13 7 13s7-8 7-13a7 7 0 0 0-7-7zm0 9.5A2.5 2.5 0 1 1 12 6.5a2.5 2.5 0 0 1 0 5z"/></svg>
        <span>4180 Harbor Crest Avenue<br>Suite 212, Port Alder CA 95021</span>
      </li>
    </ul>

    <div class="beam-illustration" role="img" aria-label="Line illustration of a crane hook lifting a steel I-beam on chains"></div>
  </section>

  <section class="card card--back">
    <div class="lockup">
      <div class="lockup__square"></div>
      <div class="lockup__divider"></div>
      <div class="wordmark">
        <div class="wordmark__name">Milo Brennick</div>
        <div class="wordmark__sub">DESIGN<small>LLC</small></div>
      </div>
    </div>
    <p class="tagline">Studio for creative architectural thought</p>
  </section>
</body>
</html>
```